Etiketten-Design für Honigglas
Zielgruppe
Wir sind eine Imkerei; unsere Zielgruppe sind Privatpersonen welche Freude am exklusiven Naturprodukt Honig haben.
Aufgabenstellung
Format:
Etikett für 250-gr.-Honigglas (TO ∅ 63 mm).
Standardmaßgrösse 165 × 40 mm
Design:
schlicht, hochwertig, modern, edel/royal, unkonventionelles Design (weg von Bienen, Waben, Landschaften usw.), dunkle Farbtöne in Kontrast zu heller Schrift, die beiden Textbausteine 'Los Nr. ' sowie 'Haltbarkeit' (siehe unten) müssen von Hand leserlich beschriftbar sein.
Inhalt (Textangaben Pflicht):
- 250 g netto
- Honig gut verschlossen, kühl (max. 15°C), dunkel und trocken lagern. Kandierten Honig nicht über 40°C erwärmen.
- Richterswiler Bienenhonig
- Los Nr.:
- Mind. haltbar bis Ende:

```html
<!DOCTYPE html>
<html lang="de">
<head>
<meta charset="utf-8">
<title>Richterswiler Bienenhonig – Etikett</title>
<link rel="stylesheet" href="https://fonts.googleapis.com/css2?family=Oswald:wght@300;400;600;700&display=swap">
<style>
  :root {
    --backdrop: #e4e4e4;
    --label-navy: #1f3a55;
    --honey-gold: #e2b22d;
    --ink-light: #f3f1ea;
    --title-cream: #fbf3d8;
    --field-white: #ffffff;
  }
  * { margin: 0; padding: 0; box-sizing: border-box; }
  html, body {
    width: 972px; height: 1200px; overflow: hidden;
    background: var(--backdrop);
  }
  body { position: relative; font-family: "Oswald", sans-serif; }

  .jar-label {
    position: absolute; left: 36px; top: 491px;
    width: 900px; height: 217px;
    background: var(--label-navy);
    box-shadow: 0 6px 18px rgba(0,0,0,0.18);
    color: var(--ink-light);
    overflow: hidden;
  }

  .storage-note {
    position: absolute; left: 36px; top: 20px; width: 160px;
    font-weight: 300; font-size: 11.5px; line-height: 14px;
    letter-spacing: 0.2px;
  }

  .net-weight {
    position: absolute; left: 36px; top: 206px;
    transform: rotate(-90deg); transform-origin: left top;
    font-weight: 600; font-size: 8.5px; letter-spacing: 0.5px;
    white-space: nowrap;
  }
  .net-weight small { font-size: 6px; }

  .field-rule {
    position: absolute; left: 49px; top: 90px;
    width: 1px; height: 116px; background: var(--honey-gold);
  }

  .write-field {
    position: absolute; left: 55px; width: 126px; height: 55px;
    background: var(--field-white);
    color: var(--label-navy);
    font-weight: 600; font-size: 7.5px; letter-spacing: 0.4px;
    padding: 3px 4px;
  }
  .write-field.lot { top: 89px; }
  .write-field.best-before { top: 151px; }

  .title-ornament {
    position: absolute; left: 282px; top: 12px;
    width: 337px; height: 172px;
    border-radius: 8px;
    background: radial-gradient(ellipse at center, rgba(226,178,45,0.22) 0%, rgba(226,178,45,0.10) 55%, rgba(31,58,85,0) 78%);
  }

  .product-title {
    position: absolute; left: 282px; top: 12px;
    width: 337px; height: 172px;
    text-align: center;
  }
  .product-title .origin {
    position: absolute; left: 58px; top: 6px;
    font-weight: 700; font-size: 17px; letter-spacing: 0.5px;
    color: var(--title-cream);
    transform: rotate(5deg);
  }
  .product-title .product {
    position: absolute; left: 10px; top: 42px;
    font-weight: 600; font-size: 60px; line-height: 1;
    letter-spacing: 0.5px;
    color: var(--title-cream);
    transform: rotate(-5deg) scaleY(1.35);
    transform-origin: left center;
    white-space: nowrap;
  }

  .maker-mark {
    position: absolute; right: 294px; top: 184px;
    text-align: right; line-height: 1;
  }
  .maker-mark .kind { display: block; font-weight: 300; font-size: 8.5px; }
  .maker-mark .name { display: block; font-weight: 600; font-size: 12px; margin-top: 2px; }

  .contact-rule {
    position: absolute; left: 708px; top: 90px;
    width: 1px; height: 116px; background: var(--honey-gold);
  }
  .contact {
    position: absolute; left: 719px; top: 94px;
    font-weight: 300; font-size: 13px;
  }
  .contact .kind { line-height: 15px; }
  .contact .name { color: var(--honey-gold); font-weight: 400; font-size: 13.5px; line-height: 16px; }
  .contact-line {
    display: flex; align-items: flex-start; gap: 7px;
    line-height: 19px; font-size: 12.5px;
  }
  .contact-line.address { margin-top: 11px; }
  .contact-line.mail { margin-top: 4px; }
  .contact-line svg { flex: none; margin-top: 5px; }
</style>
</head>
<body>
  <section class="jar-label" aria-label="Etikett Richterswiler Bienenhonig">
    <p class="storage-note">Honig gut verschlossen, kühl<br>(max. 15°C), dunkel und trocken<br>lagern. Kandierten Honig nicht<br>über 40°C erwärmen.</p>

    <p class="net-weight">250<small>GR</small> NETTO</p>
    <div class="field-rule"></div>
    <div class="write-field lot">LOSNUMMER:</div>
    <div class="write-field best-before">MIND. HALTBAR BIS ENDE:</div>

    <div class="title-ornament" role="img" aria-label="Goldene Schnörkelornamente und rundes Emblem mit Honigtropfen rund um den Titel"></div>
    <h1 class="product-title">
      <span class="origin">RICHTERSWILER</span>
      <span class="product">BIENENHONIG</span>
    </h1>

    <p class="maker-mark">
      <span class="kind">IMKEREI</span>
      <span class="name">HALDNER &amp; RÜEGG</span>
    </p>

    <div class="contact-rule"></div>
    <div class="contact">
      <p class="kind">IMKEREI</p>
      <p class="name">HALDNER &amp; RÜEGG</p>
      <div class="contact-line address">
        <svg width="8" height="11" viewBox="0 0 8 11" aria-hidden="true">
          <path d="M4 0a4 4 0 0 1 4 4c0 3-4 7-4 7S0 7 0 4a4 4 0 0 1 4-4z" fill="var(--honey-gold)"/>
          <circle cx="4" cy="4" r="1.5" fill="var(--label-navy)"/>
        </svg>
        <p>Lindenweg 12,<br>8805 Richterswil</p>
      </div>
      <div class="contact-line mail">
        <svg width="11" height="8" viewBox="0 0 11 8" aria-hidden="true">
          <rect width="11" height="8" fill="var(--honey-gold)"/>
          <path d="M0 0l5.5 4.5L11 0" fill="none" stroke="var(--label-navy)" stroke-width="1"/>
        </svg>
        <p>lupino@postfeld.ch</p>
      </div>
    </div>
  </section>
</body>
</html>
```